Corvell Advisory

Business Development Consulting Firm

Target Market(s)

Federal Government, 8(a) companies, Small Businesses

Industry/Entity Type

Private Sector, US Government

Contact Information for Business Card

8(a) Program Capture, Business Development, Industry Trends & Analysis, Strategic Teaming, Cyber Solutions

Colors

Designer to choose colors to be used in the design.

```html
<!DOCTYPE html>
<html lang="en">
<head>
<meta charset="utf-8">
<title>Corvell Advisory – Business Cards</title>
<link rel="stylesheet" href="https://fonts.googleapis.com/css2?family=Open+Sans:wght@400;600;700&family=Roboto:wght@400;500&display=swap">
<style>
  :root {
    --stage: #232323;
    --card: #1f1f23;
    --red: #7a0f12;
    --red-bright: #a3161b;
    --silver: #b4b5b9;
    --white: #ffffff;
  }
  * { box-sizing: border-box; margin: 0; padding: 0; }
  html, body {
    width: 1200px; height: 780px; overflow: hidden;
    background: var(--stage);
  }
  .canvas {
    position: relative; width: 1200px; height: 780px;
    display: flex; align-items: center; justify-content: center; gap: 40px;
  }
  .card {
    position: relative; width: 540px; height: 309px;
    background: var(--card);
    box-shadow: 0 14px 30px rgba(0,0,0,.55);
    overflow: hidden;
  }

  /* Back side */
  .card-back .pattern-field {
    position: absolute; inset: 0;
    background:
      linear-gradient(120deg, rgba(220,221,224,.35) 0%, rgba(150,151,155,.18) 22%, rgba(31,31,35,0) 42%),
      var(--card);
  }
  .card-back .brand-small {
    position: absolute; top: 26px; right: 30px;
    font-family: "Open Sans", sans-serif; font-weight: 700;
    font-size: 13px; letter-spacing: .06em; text-transform: uppercase;
    color: var(--white);
    display: flex; align-items: center; gap: 7px;
  }
  .brand-small .brand-dot {
    width: 8px; height: 8px; border-radius: 50%; background: var(--white);
  }
  .card-back .services {
    position: absolute; left: 30px; right: 30px; bottom: 26px;
    text-align: center; white-space: nowrap;
    font-family: "Roboto", sans-serif; font-size: 11px; color: var(--white);
  }
  .services .sep {
    display: inline-block; width: 5px; height: 5px; border-radius: 50%;
    background: var(--red-bright); margin: 0 6px; vertical-align: middle;
  }

  /* Front side */
  .card-front .band {
    position: absolute; inset: 0; width: 100%; height: 100%;
  }
  .card-front .brand-name {
    position: absolute; top: 44px; left: 0; right: 0;
    font-family: "Open Sans", sans-serif; font-weight: 700;
    font-size: 30px; letter-spacing: .08em; text-transform: uppercase;
    color: var(--silver);
    display: flex; justify-content: center; align-items: center; gap: 12px;
  }
  .brand-name .brand-dot {
    width: 14px; height: 14px; background: var(--red-bright);
  }
  .card-front .person {
    position: absolute; left: 36px; top: 130px; width: 240px; text-align: right;
    font-family: "Open Sans", sans-serif;
  }
  .person .person-name {
    font-size: 24px; font-weight: 700; color: var(--silver); line-height: 1.1;
  }
  .person .person-name .first { color: var(--red-bright); }
  .person .person-title {
    font-size: 13.5px; font-weight: 600; color: var(--white); margin-top: 3px;
  }
  .card-front .divider {
    position: absolute; left: 298px; top: 116px; width: 1.5px; height: 72px;
    background: var(--white);
  }
  .card-front .contacts {
    position: absolute; left: 318px; top: 118px;
    list-style: none;
    font-family: "Open Sans", sans-serif; font-size: 12.5px; color: var(--white);
  }
  .contacts li { display: flex; align-items: center; gap: 9px; height: 22px; }
  .contacts svg { width: 13px; height: 13px; flex: none; }
  .card-front .address {
    position: absolute; left: 0; right: 0; bottom: 20px; text-align: center;
    font-family: "Open Sans", sans-serif; font-size: 14px; color: var(--white);
  }
</style>
</head>
<body>
<main class="canvas">

  <section class="card card-back" aria-label="Business card back">
    <div class="pattern-field" role="img" aria-label="Repeating brand pattern with a silver sheen fading into dark glossy print"></div>
    <div class="brand-small"><span class="brand-dot"></span>Corvell Advisory</div>
    <p class="services">
      Program Capture<span class="sep"></span>Business Development<span class="sep"></span>Industry Trends &amp; Analysis<span class="sep"></span>Strategic Teaming
    </p>
  </section>

  <section class="card card-front" aria-label="Business card front">
    <svg class="band" viewBox="0 0 540 309" preserveAspectRatio="none" aria-hidden="true">
      <path d="M0 268 C200 262 400 240 540 196 L540 309 L0 309 Z" fill="var(--red)"/>
      <path d="M30 256 C220 248 410 228 528 190" fill="none" stroke="var(--silver)" stroke-width="3" stroke-linecap="round"/>
    </svg>

    <div class="brand-name"><span class="brand-dot"></span>Corvell Advisory</div>

    <div class="person">
      <p class="person-name"><span class="first">Lena</span> Havlick</p>
      <p class="person-title">Managing Director</p>
    </div>

    <div class="divider"></div>

    <ul class="contacts">
      <li>
        <svg viewBox="0 0 16 16" aria-hidden="true"><path fill="var(--red-bright)" d="M3.6 1.2l2.3 2.6-1.3 1.8c.9 1.9 2.3 3.3 4.2 4.2l1.8-1.3 2.6 2.3-1.4 2.6C6.4 13.2 2.8 9.6 1 4.2z"/></svg>
        (555) 014-2290
      </li>
      <li>
        <svg viewBox="0 0 16 16" aria-hidden="true"><rect x="1" y="3" width="14" height="10" rx="1.5" fill="var(--red-bright)"/><path d="M2 4.5l6 4.5 6-4.5" fill="none" stroke="var(--card)" stroke-width="1.3"/></svg>
        hello@corvelladvisory.com
      </li>
      <li>
        <svg viewBox="0 0 16 16" aria-hidden="true"><circle cx="8" cy="8" r="6.5" fill="none" stroke="var(--red-bright)" stroke-width="1.5"/><ellipse cx="8" cy="8" rx="2.6" ry="6.5" fill="none" stroke="var(--red-bright)" stroke-width="1.2"/><path d="M1.5 8h13" stroke="var(--red-bright)" stroke-width="1.2"/></svg>
        www.corvelladvisory.com
      </li>
    </ul>

    <p class="address">480 Maple Ridge Ave. Suite 310 Denton, TX 76201</p>
  </section>

</main>
</body>
</html>
```